Business card for our start up Automotive Shop

Clean business card design for our new automotive shop Harborline Motor Works. This card will be the template for all of our staff member including technicians and service advisors.

Harborline Motor Works is an automotive service shop catering to US domestic and asian import vehicles. We are a service and maintenance full service facility. Our aim is to provide the best quality workmanship and the best customer service experience in our industry.

Our target market are young professionals to people with families. We are not targeting a younger audience or the car modification scene. The card should be appealing to women of the 30+ age demographic.

We are a shop of younger professionals instead of an older crowd. The card design should reflect as such.

Target Market(s)

30+ Female demographic and 30+ male.

Industry/Entity Type

Automotive

Contact Information for Business Card

Must be clean and appealing to clients. Large enough and easy to read print.

Font styles to use
Sans Serif

Colors
f78f20
ffffff
b2b2b2
dddddd

Requirements
Must have
• Address, website and phone number
• 42-17 58th Ct
• Middle Village NY 11502
• (718) 555-0142
• harborlinemotorworks.example
• There must be an area to add a Name and e-mail address for personalization purposes.
Nice to have
• Back of the card should have website.
• I would also like to incorporate yelp, google+, Facebook, and instagram widgets. Will add the exact pages but everything can be @ or / harborlinemotorworks
• That can be added on the back of the card.

```html
<!DOCTYPE html>
<html lang="en">
<head>
<meta charset="utf-8">
<title>Harborline Motor Works – Business Card</title>
<link rel="stylesheet" href="https://fonts.googleapis.com/css2?family=Arimo:wght@400;700&display=swap">
<style>
  :root {
    --orange: #f78f20;
    --white: #ffffff;
    --grey: #b2b2b2;
    --light-grey: #dddddd;
    --stage: #2a2a2a;
  }
  * { box-sizing: border-box; margin: 0; padding: 0; }
  html, body {
    width: 1200px; height: 997px; overflow: hidden;
    background: var(--stage);
    font-family: "Arimo", Arial, sans-serif;
  }
  .card {
    position: absolute; left: 250px;
    width: 700px; height: 400px;
    border-radius: 22px; overflow: hidden;
  }

  /* ---------- Back ---------- */
  .card-back { top: 50px; background: var(--orange); }
  .back-brand {
    position: absolute; left: 0; right: 0; top: 150px;
    display: flex; align-items: center; justify-content: center; gap: 20px;
  }
  .brand-dot {
    width: 72px; height: 72px; border-radius: 50%;
    background: var(--white); flex: none;
  }
  .brand-name {
    font-weight: 700; font-size: 32px; letter-spacing: 1px;
    color: var(--white); text-transform: uppercase; white-space: nowrap;
  }
  .social-row {
    position: absolute; top: 262px; left: 0; right: 0;
    display: flex; justify-content: center; gap: 14px;
  }
  .social-badge {
    width: 26px; height: 26px; border-radius: 5px;
    background: var(--white); opacity: .9;
  }

  /* ---------- Front ---------- */
  .card-front { top: 540px; background: var(--white); }
  .front-brand {
    position: absolute; top: 44px; left: 0; right: 0;
    display: flex; align-items: center; justify-content: center; gap: 16px;
  }
  .front-brand .brand-dot { width: 58px; height: 58px; background: var(--orange); }
  .front-brand .brand-name { font-size: 30px; color: var(--orange); }

  .stripe { position: absolute; left: 0; right: 0; background: var(--orange); }
  .stripe-top-1 { top: 146px; height: 4px; }
  .stripe-top-2 { top: 156px; height: 4px; }
  .info-band { top: 168px; height: 160px; }
  .web-strip {
    position: absolute; left: 0; right: 0; top: 328px; height: 38px;
    background: var(--white);
    display: flex; align-items: center; justify-content: center;
  }
  .web-strip a {
    color: var(--orange); text-decoration: none;
    font-weight: 700; font-size: 16px; letter-spacing: 3px; white-space: nowrap;
  }
  .foot-band { top: 366px; height: 34px; }
  .foot-line { position: absolute; left: 0; right: 0; height: 2px; background: var(--white); }
  .foot-line-1 { top: 374px; }
  .foot-line-2 { top: 382px; }

  .person {
    position: absolute; left: 70px; top: 222px; color: var(--white);
  }
  .person-name { font-weight: 700; font-size: 22px; letter-spacing: .5px; white-space: nowrap; }
  .person-role { font-size: 16px; margin-top: 4px; padding-left: 30px; }

  .divider {
    position: absolute; left: 330px; top: 190px; width: 2px; height: 120px;
    background: linear-gradient(to bottom, transparent, var(--white), transparent);
  }

  .contact-list {
    position: absolute; left: 356px; top: 192px; list-style: none;
    color: var(--white); font-size: 14.5px; line-height: 1.45;
  }
  .contact-list li {
    display: flex; align-items: flex-start; gap: 10px; margin-bottom: 3px; white-space: nowrap;
  }
  .contact-icon {
    flex: none; width: 17px; height: 17px; border-radius: 50%;
    background: var(--white); display: flex; align-items: center; justify-content: center;
    margin-top: 2px;
  }
  .contact-icon svg { width: 11px; height: 11px; fill: var(--orange); }
</style>
</head>
<body>

  <section class="card card-back">
    <div class="back-brand">
      <span class="brand-dot"></span>
      <span class="brand-name">Harborline Motor Works</span>
    </div>
    <div class="social-row">
      <span class="social-badge" role="img" aria-label="Review listing badge"></span>
      <span class="social-badge" role="img" aria-label="Social profile badge"></span>
      <span class="social-badge" role="img" aria-label="Photo sharing badge"></span>
      <span class="social-badge" role="img" aria-label="Social network badge"></span>
    </div>
  </section>

  <section class="card card-front">
    <div class="front-brand">
      <span class="brand-dot"></span>
      <span class="brand-name">Harborline Motor Works</span>
    </div>

    <div class="stripe stripe-top-1"></div>
    <div class="stripe stripe-top-2"></div>
    <div class="stripe info-band"></div>

    <div class="person">
      <div class="person-name">MARCUS DELANEY</div>
      <div class="person-role">Managing Director</div>
    </div>

    <div class="divider"></div>

    <ul class="contact-list">
      <li>
        <span class="contact-icon"><svg viewBox="0 0 24 24"><path d="M6.6 10.8a15.1 15.1 0 0 0 6.6 6.6l2.2-2.2a1 1 0 0 1 1-.25 11.4 11.4 0 0 0 3.6.57 1 1 0 0 1 1 1V20a1 1 0 0 1-1 1A17 17 0 0 1 3 4a1 1 0 0 1 1-1h3.5a1 1 0 0 1 1 1c0 1.25.2 2.45.57 3.57a1 1 0 0 1-.25 1z"/></svg></span>
        (718) 555-0142
      </li>
      <li>
        <span class="contact-icon"><svg viewBox="0 0 24 24"><path d="M2 5h20v14H2z M2 5l10 8 10-8"/></svg></span>
        service@harborlinemotorworks.example
      </li>
      <li>
        <span class="contact-icon"><svg viewBox="0 0 24 24"><path d="M12 2a7 7 0 0 0-7 7c0 5 7 13 7 13s7-8 7-13a7 7 0 0 0-7-7zm0 9.5A2.5 2.5 0 1 1 12 6.5a2.5 2.5 0 0 1 0 5z"/></svg></span>
        <span>42-17 58th Ct, Linden Hollow<br>NY 11502</span>
      </li>
    </ul>

    <div class="web-strip"><a href="#">www.harborlinemotorworks.example</a></div>

    <div class="stripe foot-band"></div>
    <div class="foot-line foot-line-1"></div>
    <div class="foot-line foot-line-2"></div>
  </section>

</body>
</html>
```